Redesign our iOS App Design mockups

- Redesign our current Veltro App Mockup
- Keep the design simple so that programmers do not have to do too much extra work to make your design work.
- Look at the attached website screenshot for the overall look and feel, and color scheme
- Convert the attached vector logo to iOS Icon format.
- Deliver all graphics in the density required for Veltro QL Prime.
- I have attached the current iOS mockup in a .ZIP file but you can view it here as well: https://boards.mockvault.net/share/QWTRPL8HNB2

Target Market(s)

Mostly Male Internet Consumers between the ages of 20 and 35

Industry/Entity Type

Internet

Colors

Designer to choose colors to be used in the design.

Requirements
Must have
• - Deliver all graphics in the density required for Veltro QL Prime
• - Should also look good on Tabrix and Tabrix pro
• - Design type should be “FLAT.”
• - Spell out fonts used in the design and where they are used. Also, include font sizes.
• - Please use ALL the elements in each page and use all placements and text EXACTLY. Please do not improvise with text or components.
• I have designed the mockup exactly the way I like it. I just want it to made to look better.
Should not have

```html
<!DOCTYPE html>
<html lang="en">
<head>
<meta charset="utf-8">
<title>Nestline iOS App Screens</title>
<link rel="stylesheet" href="https://fonts.googleapis.com/css2?family=Nunito+Sans:wght@400;600;700;800&display=swap">
<style>
:root{
  --coral:#e5574a;
  --coral-2:#f28a4f;
  --plum:#3e2d4a;
  --plum-2:#4b3858;
  --plum-band:#3a2a45;
  --ink:#1d1d22;
  --muted:#7b7b85;
  --line:#e4e4e8;
  --panel:#ececf0;
  --keyboard:#d2d5db;
  --key:#ffffff;
  --key-dark:#abb0ba;
  --page:#ffffff;
  --green:#4cd964;
  --star:#f6b818;
}
*{box-sizing:border-box;margin:0;padding:0}
html,body{width:1200px;height:1106px;overflow:hidden;background:var(--page)}
body{position:relative;font-family:"Nunito Sans",sans-serif;color:var(--ink)}
.screen{position:absolute;width:210px;height:450px;border-radius:26px;overflow:hidden;background:#fff;box-shadow:0 0 0 1px #dcdce2}
.abs{position:absolute}
.status{position:absolute;top:10px;left:14px;right:14px;height:10px;display:flex;justify-content:space-between;font-size:8px;font-weight:700}
.status svg{width:26px;height:8px}
.title{position:absolute;top:32px;left:0;right:0;text-align:center;font-size:9px;font-weight:800}
.topbar{position:absolute;top:0;left:0;right:0;height:52px;border-bottom:1px solid var(--line)}
.brand{font-weight:800;letter-spacing:.2px;color:var(--ink)}
.brand-dot{display:inline-block;width:9px;height:9px;border-radius:50%;background:var(--coral);vertical-align:middle;margin-right:4px}
.label{font-size:5.5px;font-weight:800;letter-spacing:.3px}
.field{font-size:7px;border-bottom:1px solid var(--line);padding-bottom:4px}
.btn{position:absolute;left:8px;right:8px;height:26px;border-radius:13px;display:flex;align-items:center;justify-content:center;font-size:7px;font-weight:800;color:#fff;background:var(--coral)}
.btn-ghost{background:#fff;color:var(--ink);border:1px solid var(--line);font-weight:600;font-size:6px}
.btn-ghost b{color:var(--coral)}
.keyboard{position:absolute;left:0;right:0;bottom:0;height:162px;background:var(--keyboard);padding-top:6px}
.krow{display:flex;justify-content:center;gap:3px;margin-bottom:6px}
.k{width:17px;height:23px;background:var(--key);border-radius:4px;font-size:11px;display:flex;align-items:center;justify-content:center;box-shadow:0 1px 0 #8d929b}
.k.dark{background:var(--key-dark);width:24px;font-size:8px}
.k.wide{width:100px;font-size:7px}
.k.mid{width:48px;font-size:7px;background:var(--key-dark)}
.kfoot{display:flex;justify-content:space-between;padding:6px 14px 0;font-size:10px;color:#555}
.homebar{position:absolute;bottom:6px;left:65px;width:80px;height:3px;border-radius:2px;background:#111}
.section{background:var(--panel);font-size:5.5px;font-weight:700;color:#444;padding:9px 6px 3px}
.row{height:24px;border-bottom:1px solid var(--line);display:flex;align-items:center;padding:0 6px;font-size:6px;font-weight:700;background:#fff}
.row .flag{width:12px;height:12px;border-radius:50%;margin-right:6px;flex:none}
.row .ico{width:10px;height:10px;margin-right:6px;flex:none;color:var(--coral)}
.row .grow{flex:1}
.row .star{font-size:9px;color:#c8c8cf;margin-right:8px}
.row .star.on{color:var(--star)}
.chev{color:#a9a9b2;font-size:8px}
.menu-item{display:flex;align-items:center;gap:5px;font-size:7px;font-weight:800;color:#fff;padding:0 16px;height:24px}
.menu-item svg{width:9px;height:9px}
.opt{background:#fff;border-bottom:1px solid var(--line);padding:7px 8px;position:relative}
.opt h4{font-size:7px;font-weight:700;color:var(--plum-2)}
.opt p{font-size:5.5px;color:var(--muted);line-height:1.35}
</style>
</head>
<body>

<!-- Splash -->
<section class="screen splash" style="left:72px;top:64px;background:#f1f1f3">
  <div class="status"><span>09:41</span><svg viewBox="0 0 26 8"><rect x="0" y="5" width="2" height="3"/><rect x="3" y="3" width="2" height="5"/><rect x="6" y="1" width="2" height="7"/><rect x="17" y="1" width="9" height="6" rx="1"/></svg></div>
  <div class="abs" style="top:254px;left:0;right:0;height:196px;background:linear-gradient(#e7e7ea,#d9dade 55%,#e6e6e9)" role="img" aria-label="Faded city skyline reflected over water"></div>
  <div class="abs brand" style="top:207px;left:0;right:0;text-align:center;font-size:14px"><span class="brand-dot"></span>NESTLINE</div>
  <svg class="abs" style="top:236px;left:92px;width:26px;height:26px" viewBox="0 0 26 26"><path d="M4 13a9 9 0 0 1 18 0" fill="none" stroke="var(--coral-2)" stroke-width="2" stroke-linecap="round"/><path d="M22 13a9 9 0 0 1-9 9" fill="none" stroke="var(--coral-2)" stroke-width="2" stroke-dasharray="2 3" stroke-linecap="round"/></svg>
</section>

<!-- Login -->
<section class="screen login" style="left:352px;top:64px">
  <div class="status"><span>09:41</span><svg viewBox="0 0 26 8"><rect x="0" y="5" width="2" height="3"/><rect x="3" y="3" width="2" height="5"/><rect x="6" y="1" width="2" height="7"/><rect x="17" y="1" width="9" height="6" rx="1"/></svg></div>
  <div class="title">Login</div>
  <div class="abs" style="top:48px;left:0;right:0;border-top:1px solid var(--line)"></div>
  <div class="abs brand" style="top:92px;left:0;right:0;text-align:center;font-size:9px"><span class="brand-dot" style="width:7px;height:7px"></span>NESTLINE</div>
  <div class="abs label" style="top:114px;left:8px">USERNAME</div>
  <div class="abs field" style="top:126px;left:8px;right:10px">ExampleUser22</div>
  <div class="abs label" style="top:150px;left:8px">PASSWORD</div>
  <div class="abs field" style="top:160px;left:8px;right:10px;letter-spacing:1px;font-size:8px">●●●●●●</div>
  <div class="abs" style="top:194px;left:8px;font-size:5.5px;color:var(--coral)">Forgot Password</div>
  <div class="btn" style="top:214px">Login →</div>
  <div class="btn btn-ghost" style="top:248px">Don't have an account?&nbsp;<b>Sign up here</b></div>
  <div class="keyboard">
    <div class="krow"><span class="k">q</span><span class="k">w</span><span class="k">e</span><span class="k">r</span><span class="k">t</span><span class="k">y</span><span class="k">u</span><span class="k">i</span><span class="k">o</span><span class="k">p</span></div>
    <div class="krow"><span class="k">a</span><span class="k">s</span><span class="k">d</span><span class="k">f</span><span class="k">g</span><span class="k">h</span><span class="k">j</span><span class="k">k</span><span class="k">l</span></div>
    <div class="krow"><span class="k dark">⇧</span><span class="k">z</span><span class="k">x</span><span class="k">c</span><span class="k">v</span><span class="k">b</span><span class="k">n</span><span class="k">m</span><span class="k dark">⌫</span></div>
    <div class="krow"><span class="k mid">123</span><span class="k wide">space</span><span class="k mid">return</span></div>
    <div class="kfoot"><span>☺</span><span>🎙︎</span></div>
    <div class="homebar"></div>
  </div>
</section>

<!-- Home -->
<section class="screen home" style="left:638px;top:64px">
  <div class="status"><span>09:41</span><svg viewBox="0 0 26 8"><rect x="0" y="5" width="2" height="3"/><rect x="3" y="3" width="2" height="5"/><rect x="6" y="1" width="2" height="7"/><rect x="17" y="1" width="9" height="6" rx="1"/></svg></div>
  <svg class="abs" style="top:38px;left:8px;width:12px;height:9px" viewBox="0 0 12 9"><path d="M0 1h12M0 4.5h12M0 8h12" stroke="#333" stroke-width="1"/></svg>
  <div class="abs brand" style="top:37px;left:72px;font-size:8px">NESTLINE</div>
  <div class="abs" style="top:38px;right:8px;font-size:5.5px;font-weight:600">Ping Test ∿</div>
  <div class="abs" style="top:54px;left:0;right:0;height:20px;background:var(--plum-band);color:#fff;font-size:5.5px;display:flex;align-items:center;justify-content:center;gap:3px"><span style="width:4px;height:4px;border-radius:50%;background:var(--coral)"></span>Not Connected</div>
  <div class="btn" style="top:80px;left:6px;right:6px;height:24px;background:linear-gradient(90deg,var(--coral),var(--coral-2))">Quick Connect</div>
  <div class="abs" style="top:108px;left:0;right:0">
    <div class="section">FAVOURITES</div>
    <div class="row"><span class="flag" style="background:linear-gradient(#222 33%,#dd2b22 33% 66%,#f4c526 66%)"></span><span class="grow">Germany</span><span class="star on">★</span><span class="chev">›</span></div>
    <div class="section">SPECIALTY SERVERS</div>
    <div class="row"><svg class="ico" viewBox="0 0 10 10"><circle cx="5" cy="5" r="4" fill="none" stroke="currentColor" stroke-dasharray="1.5 1.5"/></svg><span class="grow">Streaming Servers</span><span class="chev">›</span></div>
    <div class="row"><svg class="ico" viewBox="0 0 10 10"><path d="M1 3h8l-2-2M9 7H1l2 2" fill="none" stroke="currentColor"/></svg><span class="grow">P2P Servers</span><span class="chev">›</span></div>
    <div class="row"><svg class="ico" viewBox="0 0 10 10"><circle cx="5" cy="5" r="4" fill="none" stroke="currentColor"/><circle cx="5" cy="5" r="2" fill="none" stroke="currentColor"/></svg><span class="grow">Onion over VPN</span><span class="chev">›</span></div>
    <div class="section">FAVOURITES</div>
    <div class="row"><span class="flag" style="background:linear-gradient(#c9302c 50%,#fff 50%);box-shadow:inset 5px 5px 0 -1px #2a3a8c"></span><span class="grow">USA</span><span class="star">☆</span><span class="chev">›</span></div>
    <div class="row"><span class="flag" style="background:#1f3b8c;box-shadow:inset 0 0 0 4px #1f3b8c,inset 0 0 0 6px #d52b1e"></span><span class="grow">UK</span><span class="star">☆</span><span class="chev">›</span></div>
    <div class="row"><span class="flag" style="background:radial-gradient(circle,#e23b2e 35%,#fff 36%)"></span><span class="grow">Canada</span><span class="star">☆</span><span class="chev">›</span></div>
    <div class="row"><span class="flag" style="background:linear-gradient(#f59a2d 33%,#fff 33% 66%,#1f9a3a 66%)"></span><span class="grow">India</span><span class="star">☆</span><span class="chev">›</span></div>
    <div class="row"><span class="flag" style="background:linear-gradient(90deg,#233f94 33%,#fff 33% 66%,#e43a2e 66%)"></span><span class="grow">France</span><span class="star">☆</span><span class="chev">›</span></div>
    <div class="row"><span class="flag" style="background:linear-gradient(#e33a2e 50%,#fff 50%)"></span><span class="grow">Singapore</span><span class="star">☆</span><span class="chev">›</span></div>
    <div class="row"><span class="flag" style="background:linear-gradient(#222 33%,#dd2b22 33% 66%,#f4c526 66%)"></span><span class="grow">Germany</span><span class="star on">★</span><span class="chev">›</span></div>
  </div>
</section>

<!-- Side menu -->
<section class="screen menu" style="left:918px;top:64px;background:var(--plum)">
  <div class="abs" style="top:0;right:0;width:52px;height:450px;background:#8d8a92">
    <div class="abs" style="top:0;left:0;right:0;height:55px;background:#9a979f"></div>
    <div class="abs" style="top:84px;left:0;right:8px;height:24px;border-radius:0 12px 12px 0;background:#a4473f"></div>
    <div class="abs" style="top:112px;left:0;right:0;height:22px;background:#7d7a83"></div>
    <div class="abs" style="top:160px;left:0;right:0;height:18px;background:#7d7a83"></div>
    <div class="abs" style="top:250px;left:0;right:0;height:18px;background:#7d7a83"></div>
    <div class="abs" style="top:276px;left:6px;font-size:9px;line-height:25.5px;color:#6d6a73">☆<br>☆<br>☆<br>☆<br>☆<br>☆<br><span style="color:#8a7328">★</span></div>
  </div>
  <div class="status" style="left:auto;right:14px;width:40px;justify-content:flex-end;color:#222"><svg viewBox="0 0 26 8"><rect x="0" y="5" width="2" height="3"/><rect x="3" y="3" width="2" height="5"/><rect x="6" y="1" width="2" height="7"/><rect x="17" y="1" width="9" height="6" rx="1"/></svg></div>
  <div class="abs" style="top:35px;right:6px;font-size:5.5px;font-weight:600;color:#333">Ping Test ∿</div>
  <div class="abs" style="top:0;left:0;width:158px;height:450px;background:var(--plum)">
    <div class="abs brand" style="top:30px;left:14px;font-size:11px;color:#fff"><span class="brand-dot"></span>NESTLINE</div>
    <div class="abs" style="top:28px;right:2px;font-size:13px;color:#fff">✕</div>
    <div class="abs" style="top:76px;left:0;right:0">
      <div class="menu-item" style="background:var(--plum-2)"><svg viewBox="0 0 9 9"><path d="M1 4.5L4.5 1 8 4.5V8H1z" fill="none" stroke="#fff"/></svg>HOME</div>
      <div class="menu-item" style="margin-top:4px"><svg viewBox="0 0 9 9"><circle cx="4.5" cy="4.5" r="3.2" fill="none" stroke="#fff" stroke-dasharray="1.2 .6"/><circle cx="4.5" cy="4.5" r="1.2" fill="none" stroke="#fff"/></svg>SETTINGS</div>
      <div class="menu-item"><svg viewBox="0 0 9 9"><circle cx="4.5" cy="4.5" r="3.5" fill="none" stroke="#fff"/><circle cx="4.5" cy="4.5" r="1.5" fill="none" stroke="#fff"/></svg>SUPPORT CENTRE</div>
    </div>
    <div class="abs menu-item" style="top:314px;left:0;font-weight:700"><svg viewBox="0 0 9 9"><circle cx="4.5" cy="4.5" r="3.5" fill="none" stroke="#fff"/><path d="M3 4.5h3M5 3l1.5 1.5L5 6" fill="none" stroke="#fff"/></svg>LOG OUT</div>
  </div>
</section>

<!-- Forgot password -->
<section class="screen forgot" style="left:74px;top:582px">
  <div class="status"><span>09:41</span><svg viewBox="0 0 26 8"><rect x="0" y="5" width="2" height="3"/><rect x="3" y="3" width="2" height="5"/><rect x="6" y="1" width="2" height="7"/><rect x="17" y="1" width="9" height="6" rx="1"/></svg></div>
  <div class="abs" style="top:29px;left:10px;font-size:11px">←</div>
  <div class="title">Forgot Password</div>
  <div class="abs" style="top:50px;left:0;right:0;border-top:1px solid var(--line)"></div>
  <div class="abs" style="top:64px;left:8px;font-size:9px;font-weight:700">Did you forget your password?</div>
  <div class="abs" style="top:80px;left:8px;right:10px;font-size:5.5px;line-height:1.7;color:#444">If you have forgotten your password, enter the email address associated with your account into the box below and we will send you instructions on how to reset your password to you email account.</div>
  <div class="abs label" style="top:148px;left:8px">EMAIL ADDRESS</div>
  <div class="abs field" style="top:160px;left:8px;right:10px">info@example.com</div>
  <div class="btn" style="top:248px;height:26px">Submit password reset request →</div>
  <div class="keyboard">
    <div class="krow"><span class="k">q</span><span class="k">w</span><span class="k">e</span><span class="k">r</span><span class="k">t</span><span class="k">y</span><span class="k">u</span><span class="k">i</span><span class="k">o</span><span class="k">p</span></div>
    <div class="krow"><span class="k">a</span><span class="k">s</span><span class="k">d</span><span class="k">f</span><span class="k">g</span><span class="k">h</span><span class="k">j</span><span class="k">k</span><span class="k">l</span></div>
    <div class="krow"><span class="k dark">⇧</span><span class="k">z</span><span class="k">x</span><span class="k">c</span><span class="k">v</span><span class="k">b</span><span class="k">n</span><span class="k">m</span><span class="k dark">⌫</span></div>
    <div class="krow"><span class="k mid">123</span><span class="k wide">space</span><span class="k mid">return</span></div>
    <div class="kfoot"><span>☺</span><span>🎙︎</span></div>
    <div class="homebar"></div>
  </div>
</section>

<!-- Protocols -->
<section class="screen protocols" style="left:352px;top:582px;background:var(--panel)">
  <div class="topbar" style="background:#fff"></div>
  <div class="status"><span>09:41</span><svg viewBox="0 0 26 8"><rect x="0" y="5" width="2" height="3"/><rect x="3" y="3" width="2" height="5"/><rect x="6" y="1" width="2" height="7"/><rect x="17" y="1" width="9" height="6" rx="1"/></svg></div>
  <svg class="abs" style="top:35px;left:8px;width:12px;height:9px" viewBox="0 0 12 9"><path d="M0 1h12M0 4.5h12M0 8h12" stroke="#333" stroke-width="1"/></svg>
  <div class="title">Protocols</div>
  <div class="abs" style="top:52px;left:0;right:0">
    <div class="section" style="padding-top:18px">PROTOCOL SELECTION</div>
    <div class="opt"><h4>Automatic</h4><p>Let Nestline chose the best Protocol</p><span class="abs" style="right:8px;top:10px;color:var(--coral);font-size:9px">✓</span></div>
    <div class="opt"><h4>IPSec</h4><p>The most secure protocol</p></div>
    <div class="opt"><h4>IKEv2</h4><p>The most stable protocol</p></div>
  </div>
</section>

<!-- Settings -->
<section class="screen settings" style="left:637px;top:582px;background:var(--panel)">
  <div class="topbar" style="background:#fff"></div>
  <div class="status"><span>09:41</span><svg viewBox="0 0 26 8"><rect x="0" y="5" width="2" height="3"/><rect x="3" y="3" width="2" height="5"/><rect x="6" y="1" width="2" height="7"/><rect x="17" y="1" width="9" height="6" rx="1"/></svg></div>
  <svg class="abs" style="top:35px;left:8px;width:12px;height:9px" viewBox="0 0 12 9"><path d="M0 1h12M0 4.5h12M0 8h12" stroke="#333" stroke-width="1"/></svg>
  <div class="title">Settings</div>
  <div class="abs" style="top:52px;left:0;right:0">
    <div class="section" style="padding-top:18px">APP SETTINGS</div>
    <div class="opt" style="padding:8px 8px 9px"><h4>Kill Switch</h4><p>Cuts your internet connectivity when your<br>VPN connection gets lost</p><span class="abs" style="right:8px;top:11px;width:26px;height:15px;border-radius:8px;background:var(--green)"><span class="abs" style="right:1px;top:1px;width:13px;height:13px;border-radius:50%;background:#fff"></span></span></div>
    <div class="row" style="height:29px;color:var(--plum-2)"><svg class="ico" viewBox="0 0 10 10" style="color:var(--plum-2)"><path d="M5 .5L9 2v3c0 2.5-2 4-4 4.5C3 9 1 7.5 1 5V2z" fill="currentColor"/></svg><span class="grow">Protocols</span><span class="chev">›</span></div>
    <div class="row" style="height:29px;color:var(--plum-2)"><svg class="ico" viewBox="0 0 10 10" style="color:var(--plum-2)"><circle cx="5" cy="5" r="4" fill="none" stroke="currentColor"/><path d="M3 5h4M5.5 3.5L7 5 5.5 6.5" fill="none" stroke="currentColor"/></svg><span class="grow">Logout</span><span class="chev">›</span></div>
  </div>
  <div class="abs" style="top:372px;left:0;right:0">
    <div class="row" style="height:29px;font-weight:400;color:var(--muted);font-size:6.5px"><span class="grow">Terms of Service</span><span class="chev">›</span></div>
    <div class="row" style="height:29px;font-weight:400;color:var(--muted);font-size:6.5px"><span class="grow">Privacy Policy</span><span class="chev">›</span></div>
    <div style="padding:8px;font-size:5.5px;color:var(--muted)">App Version v1.0a</div>
  </div>
</section>

</body>
</html>
```